Tidal-Cup Coffee Kiosks Webdesign project

Tidal-Cup Coffee Kiosks provides coffee carts, kiosks, and/or drive thrus depending on location. At Tidal-Cup our company focuses on offering healthy snack & drink options for people on the go as well as nutritional coaching with our daily "Cup notes." We will provide some healthy snacks as well.

We offer all organic coffee & espresso drinks,100% real fruit & vegetable smoothies, protein shakes, and healthy breakfast/snack items.

I want "balance" to be a big theme in the website design. True well-being is a balance of body (health), mind (emotional well-being) and spirit (we are a Christian based company who loves and accepts all people, sexual orientation, religions, ect)

My parents are missionaries and founded the Nicaraguan organization "Bright Harvest Outreach Nicaragua" over 11 years ago ( www.brightharvestout.org ). Tidal-Cup plans to be a financial partner to their mission so 10% of profits or 2% of total revenue, whichever is greater will go to Bright Harvest and their church plants & medical/dental clinic. I want this and info about Bright Harvest to have a page on the website.
Updates

Target Market(s)

Ages 18-54 (target coffee customer).

Industry/Entity Type

Financial

Requirements
Must have
• -Home page
-Menu page
-Locations page/contact page
-Kiosk options page (cart, kiosk & drive thru descriptions, pics, traffic & location needs, ect)
-Fundraising/Bright Harvest Outreach Nicaragua page
Nice to have
• I have a logo designed that I attached. I would like the colors to be dark brown, light brown, and a lime green. My business card is also attached.

```html
<!DOCTYPE html>
<html lang="en">
<head>
<meta charset="utf-8">
<title>Tidal-Cup Coffee Kiosks</title>
<link rel="stylesheet" href="https://fonts.googleapis.com/css2?family=Source+Sans+3:wght@300;400;600;700&display=swap">
<style>
:root{
  --brown-dark:#552a1d;
  --brown-logo:#4b2a18;
  --brown-title:#5b2a1b;
  --lime-top:#c3e26a;
  --lime-bottom:#9dcd34;
  --lime-box-top:#9fd14a;
  --lime-box-bottom:#7fbb2c;
  --white:#ffffff;
  --text:#4a3a33;
  --learn:#b3625c;
  --divider:#dcd6d2;
}
*{margin:0;padding:0;box-sizing:border-box}
html,body{width:1051px;height:1200px;overflow:hidden}
body{font-family:"Source Sans 3",sans-serif;background:var(--brown-dark);position:relative;color:var(--text)}
.top-band{position:absolute;left:0;top:0;width:1051px;height:280px;background:linear-gradient(var(--lime-top),var(--lime-bottom));border-top:5px solid var(--brown-dark)}
.brand{position:absolute;left:68px;top:18px;width:175px;text-align:center}
.brand-dot{display:block;width:46px;height:46px;border-radius:50%;background:var(--brown-logo);margin:0 auto 6px}
.brand-name{font-size:42px;font-weight:600;color:var(--brown-logo);line-height:1;letter-spacing:-0.5px}
.order{position:absolute;left:815px;top:5px;width:162px;height:64px;background:var(--brown-dark);border-radius:0 0 4px 4px;color:var(--white);padding:8px 0 0 18px}
.order-label{font-size:15px;line-height:1.1}
.order-phone{font-size:22px;line-height:1.2}
.main-nav{position:absolute;left:300px;top:89px;display:flex;font-size:18px;color:var(--brown-logo)}
.main-nav span{padding:0 9px;border-left:1px solid rgba(90,50,30,.35);line-height:22px}
.main-nav span:first-child{border-left:none}
.panel{position:absolute;left:61px;top:137px;width:927px;height:946px;background:var(--white)}
.hero{position:absolute;left:70px;top:149px;width:909px;height:362px;background:radial-gradient(circle at 30% 45%,#e9e3dc 0 14%,transparent 15%),linear-gradient(120deg,#6a3a22,#3a1d10 45%,#7b5a3a 80%,#a8895f)}
.hero-text{position:absolute;left:518px;top:225px;color:var(--white);line-height:1.05;text-shadow:0 1px 3px rgba(0,0,0,.4)}
.hero-text .l1{font-size:35px;font-weight:600}
.hero-text .l2{font-size:43px;font-weight:600}
.hero-arrows{position:absolute;left:862px;top:328px}
.thumb{position:absolute;top:526px;width:284px;height:132px}
.thumb-smoothie{left:85px;background:linear-gradient(90deg,#d9c7a4,#f2b8a8 55%,#a81419)}
.thumb-latte{left:383px;background:radial-gradient(ellipse at 58% 45%,#c88e58 0 25%,#eeeae6 45%,#d5d2d2)}
.thumb-cherries{left:681px;background:linear-gradient(120deg,#3c6a1e,#9cbf3c 55%,#e4dca0)}
.about{position:absolute;left:88px;top:694px;width:575px}
.about h1{font-size:24px;font-weight:400;color:var(--brown-title);line-height:1.2}
.about h2{font-size:15.5px;font-weight:400;color:var(--brown-title);margin-top:6px}
.about p{font-size:12px;font-weight:300;line-height:20px;margin-top:6px;color:#5a4a43}
.feature{position:absolute;top:855px;width:180px}
.feature-img{height:90px;width:140px;border-radius:45%}
.feature h3{font-size:16.5px;font-weight:400;color:var(--brown-title);line-height:23px;margin-top:20px}
.feature p{font-size:12px;font-weight:300;margin-top:6px}
.feature .learn{font-size:11px;color:var(--learn);margin-top:5px;display:block}
.f-beans{left:88px}.f-beans .feature-img{background:radial-gradient(circle,#6a3a1c,#3f7a26 60%,transparent 70%)}
.f-fruit{left:298px}.f-fruit .feature-img{background:radial-gradient(circle,#f3f0c8 0 15%,#8cc43a 30%,#5d8a24 55%,transparent 70%)}
.f-seminars{left:502px;top:861px}.f-seminars .feature-img{background:radial-gradient(circle,#c98b54,#e65b4e 50%,transparent 68%)}
.divider{position:absolute;top:850px;width:1px;height:195px;background:var(--divider)}
.partner{position:absolute;left:714px;top:707px;width:254px;height:297px;border:1px solid #ddd;border-radius:12px 12px 0 0;overflow:hidden;background:var(--white)}
.partner-mark{height:133px;display:flex;align-items:center;justify-content:center;gap:8px}
.partner-mark .dot{width:14px;height:14px;background:#f2a31d;border-radius:50%}
.partner-mark .name{font-size:24px;font-weight:600;color:#2b2e7c}
.partner-info{height:164px;background:linear-gradient(var(--lime-box-top),var(--lime-box-bottom));color:var(--white);padding:14px 0 0 33px}
.partner-info .big{font-size:25px;line-height:1.1}
.partner-info .small{font-size:13.5px;margin-top:2px}
.partner-info .org{font-size:22px;font-weight:700;line-height:1.1;margin-top:4px}
.partner-info .url{font-size:12px;color:#ecf6da;margin-top:10px}
.footer-nav{position:absolute;left:63px;top:1116px;font-size:13px;color:var(--white);letter-spacing:.2px}
.footer-nav span{padding:0 5px;border-left:1px solid var(--white)}
.footer-nav span:first-child{padding-left:0;border-left:none}
.copyright{position:absolute;left:66px;top:1147px;font-size:11px;color:#e8dcd6}
.social{position:absolute;left:868px;top:1111px;display:flex;gap:3px}
.social i{display:block;width:27px;height:27px;border-radius:50%;background:var(--white)}
</style>
</head>
<body>
<div class="top-band"></div>

<div class="brand">
  <span class="brand-dot"></span>
  <div class="brand-name">Tidal-Cup</div>
</div>

<div class="order">
  <div class="order-label">Order Now</div>
  <div class="order-phone">555-010-4477</div>
</div>

<nav class="main-nav">
  <span>Home</span><span>Menu</span><span>Locations</span><span>Franchise</span><span>Fundraising</span><span>Health</span><span>Education</span><span>Contact</span>
</nav>

<div class="panel"></div>

<div class="hero" role="img" aria-label="Steaming white coffee cup with cinnamon sticks and star anise among roasted coffee beans and a burlap sack"></div>
<div class="hero-text"><div class="l1">Break the fast!</div><div class="l2">Boost metabolism!</div></div>
<svg class="hero-arrows" width="40" height="24" viewBox="0 0 40 24">
  <polyline points="14,3 5,12 14,21" fill="none" stroke="#fff" stroke-width="3.5"/>
  <polyline points="26,3 35,12 26,21" fill="none" stroke="#fff" stroke-width="3.5"/>
</svg>

<div class="thumb thumb-smoothie" role="img" aria-label="Smiling woman drinking a fruit smoothie"></div>
<div class="thumb thumb-latte" role="img" aria-label="Cappuccino with a cocoa heart on top"></div>
<div class="thumb thumb-cherries" role="img" aria-label="Ripening coffee cherries on a branch"></div>

<section class="about">
  <h1>About Us</h1>
  <h2>Duis tincidunt lectus quis dui viverra vestibulum.</h2>
  <p>Suspendisse vulputate aliquam dui. Nulla elementum dui ut augue. Aliquam vehicula mi at mauris. Maecenas placerat, nisl at consequat rhoncus, sem nunc gravida justo, quis eleifend arcu velit quis lacus. Morbi magna magna, tincidunt a, mattis non, imperdiet vitae, tellus. Sed odio est, auctor ac, sollicitudin in, consequat</p>
</section>

<div class="feature f-beans">
  <div class="feature-img" role="img" aria-label="Roasted coffee beans with green leaves"></div>
  <h3>Certified Organic<br>Nicaraguan Beans</h3>
  <p>Nunc tempus felis vitae urna.</p>
  <span class="learn">LEARN MORE</span>
</div>
<div class="divider" style="left:275px"></div>
<div class="feature f-fruit">
  <div class="feature-img" role="img" aria-label="Two halves of a kiwi fruit"></div>
  <h3>100% real fruit<br>&amp; vegetables</h3>
  <p>Nunc tempus felis vitae urna.</p>
  <span class="learn">LEARN MORE</span>
</div>
<div class="divider" style="left:477px"></div>
<div class="feature f-seminars">
  <div class="feature-img" role="img" aria-label="Bowl of muesli with berries and a spoon"></div>
  <h3>Health Education<br>Seminars</h3>
  <p>Nunc tempus felis vitae urna.</p>
  <span class="learn">LEARN MORE</span>
</div>

<aside class="partner">
  <div class="partner-mark"><span class="dot"></span><span class="name">Bright Harvest</span></div>
  <div class="partner-info">
    <div class="big">10% of all profits</div>
    <div class="small">will be sent to</div>
    <div class="org">Bright Harvest Outreach Nicaragua</div>
    <div class="url">www.brightharvestout.org</div>
  </div>
</aside>

<nav class="footer-nav">
  <span>HOME</span><span>MENU</span><span>LOCATIONS</span><span>FRANCHISE</span><span>FUNDRAISING</span><span>HEALTH</span><span>EDUCATION</span><span>CONTACT</span>
</nav>
<div class="copyright">© 2013 Company Name.&nbsp; All right reserved.</div>
<div class="social" aria-label="Social links"><i></i><i></i><i></i><i></i></div>
</body>
</html>
```